Need a book cover design for book titled: Resting Beside the River--Simple Methods for the Crossing

This book describes and presents tools to connect with and activate the Lightbody that we all carry within us. It talks about the Lighbody, brief history, lightbody levels and offers exercises to bring light into the body.
I envision a design that shows a physical body changing into light /surrounded by light; a resurrected body ascending to higher dimensions of Spirit o anything comparable .
Updates

Target Market(s)

Mature audience of spiritual seekers and those on spiritual path

Requirements
Must have
• Space on backcover for book summary at top and title and author name on spine.

```html
<!DOCTYPE html>
<html lang="en">
<head>
<meta charset="utf-8">
<title>Resting Beside the River — Book Cover</title>
<link href="https://fonts.googleapis.com/css2?family=Cinzel:wght@400;500&family=Cormorant+Garamond:ital,wght@0,500;1,500&display=swap" rel="stylesheet">
<style>
  :root {
    --page-bg: #ffffff;
    --cover-deep: #141f24;
    --cover-mid: #1f4a5a;
    --cover-teal: #3f8aa2;
    --cover-glow: #dff3fa;
    --title-ink: #ffffff;
  }
  * { margin: 0; padding: 0; box-sizing: border-box; }
  html, body {
    width: 960px;
    height: 1200px;
    overflow: hidden;
    background: var(--page-bg);
  }
  .canvas {
    position: relative;
    width: 960px;
    height: 1200px;
  }
  .cover {
    position: absolute;
    left: 100px;
    top: 30px;
    width: 760px;
    height: 1140px;
    overflow: hidden;
    background: var(--cover-deep);
  }
  .cover-art {
    position: absolute;
    inset: 0;
    background:
      radial-gradient(ellipse 22% 14% at 43% 5%, rgba(255,255,255,0.95), rgba(223,243,250,0) 100%),
      radial-gradient(ellipse 24% 16% at 44% 44%, rgba(255,255,255,0.9), rgba(223,243,250,0) 100%),
      radial-gradient(ellipse 55% 45% at 44% 35%, rgba(120,185,205,0.75), rgba(63,138,162,0) 100%),
      radial-gradient(ellipse 90% 70% at 50% 30%, var(--cover-teal), var(--cover-mid) 55%, var(--cover-deep) 100%);
  }
  .cover-art::after {
    content: "";
    position: absolute;
    left: 0; right: 0; bottom: 0;
    height: 40%;
    background: linear-gradient(to bottom, rgba(20,31,36,0), var(--cover-deep));
  }
  .light-streak {
    position: absolute;
    left: 60px;
    top: 862px;
    width: 640px;
    height: 4px;
    border-radius: 2px;
    background: radial-gradient(ellipse at 48% 50%, #e9fbff 0%, rgba(120,220,240,0.6) 20%, rgba(120,220,240,0) 70%);
  }
  .title {
    position: absolute;
    left: 0;
    right: 0;
    top: 750px;
    text-align: center;
    color: var(--title-ink);
  }
  .title-lead {
    display: block;
    font-size: 70px;
    line-height: 1;
    letter-spacing: 0.5px;
  }
  .title-lead .caps {
    font-family: "Cinzel", "Times New Roman", serif;
    font-weight: 500;
  }
  .title-lead .italic {
    font-family: "Cormorant Garamond", "Times New Roman", serif;
    font-style: italic;
    font-weight: 500;
  }
  .title-main {
    display: block;
    font-family: "Cinzel", "Times New Roman", serif;
    font-weight: 400;
    font-size: 186px;
    line-height: 1;
    letter-spacing: 6px;
    margin-top: 2px;
  }
  .subtitle {
    position: absolute;
    left: 0;
    right: 0;
    top: 1020px;
    text-align: center;
    color: var(--title-ink);
    font-family: "Cormorant Garamond", "Times New Roman", serif;
    font-weight: 500;
    font-size: 40px;
    line-height: 1;
  }
  .subtitle em { font-style: italic; }
</style>
</head>
<body>
  <div class="canvas">
    <section class="cover">
      <div class="cover-art" role="img" aria-label="Cover artwork: a human figure dissolving into dust and light, glowing from the crown and the heart, amid misty blue-teal particles"></div>
      <div class="light-streak"></div>
      <h1 class="title">
        <span class="title-lead"><span class="caps">RESTING</span> <span class="italic">Beside the</span></span>
        <span class="title-main">RIVER</span>
      </h1>
      <p class="subtitle"><em>Simple Methods for</em> the Crossing</p>
    </section>
  </div>
</body>
</html>
```